We require a banner design for a 53' x 10' trailer for a future development to be displayed on the side of the highway. The development name is 712 35 Commerce Park, logo is attached. This is an industrial future development. Please also include the RLW Group logo and MERO Development logos as well.

Industry/Entity Type

Real Estate / Construction / Developer / Industrial Future Development

Requirements
Must have
• Logos provided

```html
<!DOCTYPE html>
<html lang="en">
<head>
<meta charset="utf-8">
<title>712 35 Commerce Park – Trailer Banner</title>
<link rel="stylesheet" href="https://fonts.googleapis.com/css2?family=Montserrat:wght@400;500;600;700;800&family=Roboto+Condensed:wght@300;700&display=swap">
<style>
  :root {
    --backdrop: #b3b3b3;
    --paper: #ffffff;
    --navy: #1f3a6e;
    --navy-deep: #18305c;
    --ink: #231f20;
    --slate: #5b6690;
    --stripe: #ececec;
    --sky-light: #eef4f8;
    --sky-mid: #cfdfeb;
    --soil: #6b5140;
    --skin: #d9a48c;
    --city: #c9b08e;
  }
  * { margin: 0; padding: 0; box-sizing: border-box; }
  html, body { width: 1200px; height: 324px; overflow: hidden; background: var(--backdrop); }
  .banner {
    position: absolute; left: 77px; top: 63px; width: 1047px; height: 197px;
    background: var(--paper); overflow: hidden;
    box-shadow: 0 6px 14px rgba(0,0,0,.25);
    font-family: "Montserrat", sans-serif; color: var(--ink);
  }
  .diagonal-band { position: absolute; inset: 0; }

  .hero-visual {
    position: absolute; left: 280px; top: 0; width: 530px; height: 197px;
    background:
      radial-gradient(ellipse 34% 18% at 33% 40%, rgba(201,176,142,.9) 0%, rgba(201,176,142,0) 100%),
      radial-gradient(ellipse 32% 16% at 36% 60%, rgba(107,81,64,.85) 0%, rgba(107,81,64,0) 100%),
      radial-gradient(ellipse 42% 34% at 72% 62%, rgba(217,164,140,.85) 0%, rgba(217,164,140,0) 100%),
      radial-gradient(ellipse 60% 70% at 50% 55%, var(--sky-mid) 0%, var(--sky-light) 60%, rgba(255,255,255,0) 100%);
  }

  .swoosh { position: absolute; left: 200px; top: 0; width: 170px; height: 197px; }

  .brand-mark { position: absolute; left: 22px; top: 14px; font-weight: 800; color: var(--ink); line-height: .92; }
  .brand-mark .num { display: block; font-size: 52px; letter-spacing: 1px; }
  .brand-mark .num + .num { margin-left: 72px; }
  .brand-mark .park { display: block; font-size: 15px; letter-spacing: 2.2px; margin-top: 8px; font-weight: 500; }

  .web-pill {
    position: absolute; left: 22px; top: 136px; width: 157px; height: 26px;
    background: var(--navy); color: #fff; border-radius: 13px;
    font-size: 10px; letter-spacing: .3px; display: flex; align-items: center; justify-content: center;
  }
  .web-pill b { font-weight: 700; }

  .contact-row { position: absolute; left: 22px; top: 175px; display: flex; gap: 12px; font-size: 8px; font-weight: 600; color: var(--ink); }
  .contact-row span { display: flex; align-items: center; gap: 5px; }
  .contact-row svg { width: 14px; height: 14px; }

  .headline {
    position: absolute; left: 290px; top: 14px; width: 470px;
    font-family: "Roboto Condensed", sans-serif; font-size: 27px; color: var(--navy-deep);
    white-space: nowrap; letter-spacing: .2px;
  }
  .headline .light { font-weight: 300; }
  .headline .bold { font-weight: 700; }

  .launch { position: absolute; left: 827px; top: 34px; width: 205px; }
  .launch .coming { font-size: 23px; font-weight: 700; color: var(--navy); letter-spacing: .5px; display: flex; align-items: center; justify-content: space-between; }
  .launch .soon { background: var(--navy); color: #fff; font-weight: 500; padding: 2px 6px; border-radius: 4px; }
  .launch .to { margin-top: 8px; text-align: center; font-size: 17px; font-weight: 500; }
  .launch .to b { font-weight: 700; }

  .rule { position: absolute; left: 827px; top: 106px; width: 204px; height: 1px; background: var(--ink); }
  .divider { position: absolute; left: 953px; top: 114px; width: 1px; height: 72px; background: var(--ink); }

  .partner { position: absolute; color: var(--ink); display: flex; align-items: center; gap: 10px; font-weight: 500; }
  .partner.mero { left: 827px; top: 122px; font-size: 19px; letter-spacing: 4px; }
  .partner.mero i { width: 30px; height: 30px; border: 2px solid var(--navy); display: block; }
  .partner.rlw { left: 962px; top: 129px; font-size: 19px; gap: 7px; }
  .partner.rlw i { width: 12px; height: 12px; border-radius: 50%; background: var(--navy); display: block; }

  .phone { position: absolute; left: 827px; top: 164px; display: flex; align-items: center; gap: 8px; font-size: 14.5px; font-weight: 500; }
  .phone .icon { width: 23px; height: 23px; border-radius: 50%; background: var(--navy); display: flex; align-items: center; justify-content: center; }

  .socials { position: absolute; left: 962px; top: 168px; width: 70px; display: flex; justify-content: space-between; font-size: 8px; font-weight: 600; color: var(--ink); }
</style>
</head>
<body>
<main class="banner">
  <svg class="diagonal-band" viewBox="0 0 1047 197" aria-hidden="true">
    <polygon points="1000,0 1047,0 1047,20 880,197 800,197" fill="var(--stripe)"/>
  </svg>

  <div class="hero-visual" role="img" aria-label="Open hand holding a floating slab of land topped with a small city of buildings and trees, against a pale sky"></div>

  <svg class="swoosh" viewBox="0 0 170 197" aria-hidden="true">
    <path d="M0,0 H70 C35,50 60,95 110,140 C150,175 140,190 120,197 H0 Z" fill="var(--paper)"/>
    <path d="M70,0 C35,50 60,95 110,140 C150,175 140,190 120,197" fill="none" stroke="var(--slate)" stroke-width="5"/>
    <path d="M78,0 C46,50 70,95 120,140 C160,175 150,190 132,197" fill="none" stroke="var(--navy)" stroke-width="4"/>
    <path d="M88,0 C58,48 82,92 130,138" fill="none" stroke="var(--navy)" stroke-width="1.5" opacity=".6"/>
  </svg>

  <div class="brand-mark">
    <span class="num">712</span>
    <span class="num">35</span>
    <span class="park">COMMERCE PARK</span>
  </div>

  <div class="web-pill">WWW.<b>YOURWEBSITE</b>.COM</div>

  <div class="contact-row">
    <span>
      <svg viewBox="0 0 14 14" aria-hidden="true"><circle cx="7" cy="7" r="7" fill="var(--navy)"/><path d="M7 3.2a2.4 2.4 0 0 0-2.4 2.4C4.6 7.4 7 10.6 7 10.6s2.4-3.2 2.4-5A2.4 2.4 0 0 0 7 3.2z" fill="none" stroke="#fff" stroke-width=".9"/><circle cx="7" cy="5.6" r=".8" fill="#fff"/></svg>
      YOUR LOCATION HERE
    </span>
    <span>
      <svg viewBox="0 0 14 14" aria-hidden="true"><circle cx="7" cy="7" r="7" fill="var(--navy)"/><rect x="3.8" y="4.8" width="6.4" height="4.4" fill="none" stroke="#fff" stroke-width=".8"/><path d="M3.8 4.8 7 7.4l3.2-2.6" fill="none" stroke="#fff" stroke-width=".8"/></svg>
      YOUR EMAIL HERE
    </span>
  </div>

  <h1 class="headline"><span class="light">YOUR BUSINESS’S </span><span class="bold">FUTURE DESTINATION!</span></h1>

  <div class="launch">
    <div class="coming">COMING <span class="soon">SOON</span></div>
    <div class="to">to <b>This Location!</b></div>
  </div>

  <div class="rule"></div>
  <div class="divider"></div>

  <div class="partner mero"><i></i>MERO</div>
  <div class="partner rlw"><i></i>RLW</div>

  <div class="phone">
    <span class="icon">
      <svg width="12" height="12" viewBox="0 0 12 12" aria-hidden="true"><path d="M3 1.5l1.6 2.2-1 1.1a6 6 0 0 0 3.6 3.6l1.1-1L10.5 9 9.6 10.3C5.4 10.3 1.7 6.6 1.7 2.4z" fill="#fff"/></svg>
    </span>
    123 456 789
  </div>

  <div class="socials"><span>Kibo</span><span>Zap</span><span>Vio</span></div>
</main>
</body>
</html>
```